Brookfarrow Osteopathy and dry needling business card

Business card for Brookfarrow Osteopathy and Dry Needling.

Industry/Entity Type

Health

Contact Information for Business Card

I do not have a phone number yet. I also do not have an email address yet. The physical address is: 48 Lower Crane Street Brookfarrow The website is: www.brookfarrowosteosteopathy.example My details are: Dr Martin Pellowe, Osteopath (B.Clin.Sci (Ost) M.Ost BSC ECON (Hons)

Colors
0094D4
00A9DD
6FCCEA
C7EBF8
E9F6FB

Requirements
Must have
• logo on the back
Nice to have
• Maybe a space for me to write an appointment time and date on the card.

```html
<!DOCTYPE html>
<html lang="en">
<head>
<meta charset="utf-8">
<title>Brookfarrow Osteopathy and Dry Needling – Business Card</title>
<link href="https://fonts.googleapis.com/css2?family=Montserrat:wght@500;600;700;800&family=Arimo:wght@400;700&display=swap" rel="stylesheet">
<style>
  :root {
    --stage: #1d1d20;
    --card: #2b2b2e;
    --card-edge: #333337;
    --brand-blue: #0094d4;
    --brand-cyan: #00a9dd;
    --brand-sky: #6fccea;
    --field: #ffffff;
    --text-light: #f2f2f2;
    --text-muted: #d6d6d6;
    --emboss: #3a3a3e;
  }
  * { box-sizing: border-box; margin: 0; padding: 0; }
  html, body {
    width: 1200px; height: 886px; overflow: hidden;
    background: var(--stage);
  }
  .canvas {
    width: 1200px; height: 886px;
    display: flex; flex-direction: column; align-items: center; justify-content: center;
    gap: 40px;
  }
  .card {
    position: relative;
    width: 620px; height: 354px;
    background: var(--card);
    border-radius: 26px;
    box-shadow: 0 0 0 1px var(--card-edge);
    overflow: hidden;
    font-family: "Arimo", Arial, sans-serif;
  }

  /* Appointment side */
  .appointment__title {
    position: absolute; left: 0; right: 0; top: 38px;
    text-align: center;
    font-family: "Montserrat", sans-serif; font-weight: 800;
    font-size: 40px; letter-spacing: 1px;
    color: var(--brand-blue);
  }
  .field-label {
    position: absolute;
    font-family: "Montserrat", sans-serif; font-weight: 700;
    font-size: 15px; color: var(--brand-blue);
  }
  .field {
    position: absolute; height: 36px;
    background: var(--field); border-radius: 7px;
  }
  .days {
    position: absolute; left: 56px; right: 56px; bottom: 40px;
    display: flex; justify-content: space-between;
    list-style: none;
  }
  .day {
    display: flex; align-items: center; gap: 8px;
    font-family: "Montserrat", sans-serif; font-weight: 500;
    font-size: 15px; color: var(--brand-blue);
  }
  .day__box { width: 15px; height: 15px; background: var(--field); }

  /* Contact side */
  .accent-bar {
    position: absolute; right: 0; top: 26px;
    width: 12px; height: 54px; background: var(--brand-blue);
  }
  .practitioner {
    position: absolute; right: 36px; top: 26px; text-align: right;
  }
  .practitioner__name {
    font-family: "Montserrat", sans-serif; font-weight: 700;
    font-size: 21px; color: var(--brand-blue);
  }
  .practitioner__role {
    font-size: 15px; line-height: 1.3; color: var(--text-light); margin-top: 3px;
  }
  .brand-mark {
    position: absolute; left: 40px; top: 48px;
    display: flex; align-items: center; gap: 12px;
    width: 250px;
  }
  .brand-mark__dot {
    flex: none; width: 22px; height: 22px; border-radius: 50%;
    background: var(--brand-blue);
  }
  .brand-mark__name {
    font-family: "Arimo", Arial, sans-serif; font-weight: 700;
    font-size: 19px; line-height: 1.25; color: var(--brand-blue);
  }
  .emboss-name {
    position: absolute; right: 40px; top: 150px; width: 240px;
    text-align: right;
    font-family: "Arimo", Arial, sans-serif; font-weight: 700;
    font-size: 30px; line-height: 1.15; color: var(--emboss);
  }
  .address {
    position: absolute; left: 40px; top: 200px;
    font-size: 19px; line-height: 1.3; color: var(--text-light);
  }
  .contact-list {
    position: absolute; left: 40px; bottom: 28px;
    list-style: none; font-size: 17px; color: var(--text-light);
  }
  .contact-list li { display: flex; align-items: center; gap: 10px; line-height: 1.45; }
  .contact-list svg { width: 15px; height: 15px; flex: none; }
</style>
</head>
<body>
<main class="canvas">

  <section class="card card--appointment" aria-label="Appointment side">
    <h2 class="appointment__title">APPOINTMENT</h2>

    <span class="field-label" style="left:56px; top:134px;">Name :</span>
    <div class="field" style="left:124px; top:124px; width:440px;"></div>

    <span class="field-label" style="left:56px; top:200px;">DATE :</span>
    <div class="field" style="left:120px; top:190px; width:200px;"></div>

    <span class="field-label" style="left:342px; top:200px;">TIME :</span>
    <div class="field" style="left:404px; top:190px; width:160px;"></div>

    <ul class="days">
      <li class="day"><span class="day__box"></span>MON</li>
      <li class="day"><span class="day__box"></span>TUE</li>
      <li class="day"><span class="day__box"></span>WED</li>
      <li class="day"><span class="day__box"></span>THU</li>
      <li class="day"><span class="day__box"></span>FRI</li>
      <li class="day"><span class="day__box"></span>SAT</li>
    </ul>
  </section>

  <section class="card card--contact" aria-label="Contact side">
    <div class="accent-bar"></div>
    <div class="practitioner">
      <p class="practitioner__name">Dr Martin Pellowe</p>
      <p class="practitioner__role">Osteopath (B.Clin.Sci (Ost)<br>M.Ost BSC ECON (Hons)</p>
    </div>

    <div class="brand-mark">
      <span class="brand-mark__dot"></span>
      <span class="brand-mark__name">Brookfarrow Osteopathy<br>and Dry Needling</span>
    </div>

    <p class="emboss-name" aria-hidden="true">Brookfarrow Osteopathy</p>

    <p class="address">48 Lower Crane Street<br>Brookfarrow</p>

    <ul class="contact-list">
      <li>
        <svg viewBox="0 0 16 16"><path fill="var(--brand-cyan)" d="M3.5 1.5l3 3-1.6 1.8c.9 1.9 2.4 3.4 4.3 4.3l1.8-1.6 3 3-2 2C6.5 13.5 2.5 9.5 1.5 3.5z"/></svg>
        555-010-2100
      </li>
      <li>
        <svg viewBox="0 0 16 16"><rect x="1" y="3" width="14" height="10" rx="1.5" fill="var(--brand-cyan)"/><path d="M1.5 4l6.5 5 6.5-5" fill="none" stroke="var(--card)" stroke-width="1.4"/></svg>
        hello@brookfarrow.example
      </li>
      <li>
        <svg viewBox="0 0 16 16"><circle cx="8" cy="8" r="7" fill="var(--brand-cyan)"/><path d="M1 8h14M8 1c-3 3.5-3 10.5 0 14M8 1c3 3.5 3 10.5 0 14" fill="none" stroke="var(--card)" stroke-width="1.2"/></svg>
        www.brookfarrowosteosteopathy.example
      </li>
    </ul>
  </section>

</main>
</body>
</html>
```